Plumbing Product Supply Company Needs Front & Back Cover Design For Instruction Manuals

We need a front and back over design for our instruction manuals that we need to give to clients.

There will also be a picture of the product on the front cover so please use the supplied image as dummy.

it needs to incorporate our logo and branding colours.

We are the industry leader so it needs to be up-market, professional and stand out from the crowd.

Target Market(s)

Plumbing Companies

Industry/Entity Type

Plumbing

Font styles to use
Sans Serif

Colors
abd036
ffffff
000000
eaeaea
cbcbcb

Requirements
Must have
• Front & Back Cover as it will become a booklet.
• The logo is to be on the black background.
Nice to have
• Professional, modern, sleek.
Should not have
• Other colours that what is on the guidelines.

```html
<!DOCTYPE html>
<html lang="en">
<head>
<meta charset="utf-8">
<title>Meridian Pipeline Supplies – Instruction Manual Covers</title>
<link rel="stylesheet" href="https://fonts.googleapis.com/css2?family=Josefin+Sans:wght@300;600&family=Open+Sans:wght@700&display=swap">
<style>
  :root {
    --brand-green: #abd036;
    --brand-green-light: #b9d94f;
    --ink: #1f2021;
    --charcoal: #2a2b2d;
    --silver: #cbcbcb;
    --mist: #eaeaea;
    --white: #ffffff;
    --backdrop: #e8dfdb;
    --photo-earth: #b07a4c;
    --photo-sand: #d9c4a4;
  }
  html, body {
    margin: 0;
    width: 1200px;
    height: 940px;
    overflow: hidden;
    background: var(--backdrop);
  }
  .spread {
    position: absolute;
    left: 80px;
    top: 102px;
    width: 1040px;
    height: 736px;
    display: flex;
    box-shadow: 0 18px 40px rgba(60, 40, 30, 0.18);
  }
  .cover { width: 520px; height: 736px; display: block; }
  .brand-name {
    font-family: "Josefin Sans", sans-serif;
    font-weight: 600;
    fill: var(--ink);
  }
  .contact {
    font-family: "Open Sans", sans-serif;
    font-weight: 700;
    fill: var(--ink);
  }
  .web-tab-text {
    font-family: "Open Sans", sans-serif;
    font-weight: 700;
    font-size: 10px;
    fill: var(--white);
    letter-spacing: 0.3px;
  }
  .title-main {
    font-family: "Josefin Sans", sans-serif;
    font-weight: 300;
    fill: var(--ink);
  }
</style>
</head>
<body>
<main class="spread">

  <!-- Back cover -->
  <svg class="cover cover--back" viewBox="0 0 520 736" xmlns="http://www.w3.org/2000/svg">
    <defs>
      <linearGradient id="greenFieldBack" x1="0" y1="0" x2="1" y2="1">
        <stop offset="0" stop-color="var(--brand-green-light)"/>
        <stop offset="1" stop-color="var(--brand-green)"/>
      </linearGradient>
      <linearGradient id="productPhoto" x1="0" y1="0" x2="1" y2="0">
        <stop offset="0" stop-color="var(--photo-sand)"/>
        <stop offset="0.45" stop-color="var(--photo-earth)"/>
        <stop offset="0.8" stop-color="#7fbf3a"/>
        <stop offset="1" stop-color="var(--photo-earth)"/>
      </linearGradient>
    </defs>
    <rect class="page-field" width="520" height="736" fill="url(#greenFieldBack)"/>

    <g class="brand-lockup">
      <text class="brand-name" x="260" y="120" font-size="46" text-anchor="middle" letter-spacing="4">MERIDIAN</text>
      <text class="brand-name" x="260" y="152" font-size="20" text-anchor="middle" letter-spacing="2">PIPELINE SUPPLIES</text>
    </g>

    <path class="curve-line" d="M0,300 Q250,272 520,398" fill="none" stroke="var(--charcoal)" stroke-width="9"/>
    <path class="product-photo" role="img" aria-label="Photo of a green pipe-lining bladder inserted in an excavated clay pipe"
          d="M0,322 Q250,296 520,418 L520,474 Q260,498 0,540 Z" fill="url(#productPhoto)"/>
    <path class="curve-line" d="M0,558 Q260,516 520,490" fill="none" stroke="var(--charcoal)" stroke-width="5"/>

    <g class="contact-block" text-anchor="middle">
      <text class="contact" x="260" y="624" font-size="15">MERIDIAN PIPE LINING SUPPLIERS LTD.</text>
      <text class="contact" x="260" y="644" font-size="11">Harbour Lane Westfield NSW 2100</text>
      <text class="contact" x="260" y="668" font-size="18">Tel: 1-300-555-019</text>
      <text class="contact" x="260" y="686" font-size="11">ABN : 00 123 456 789</text>
    </g>

    <path class="footer-band" d="M0,736 L0,716 L200,716 Q380,706 520,668 L520,736 Z" fill="var(--silver)"/>
    <path class="footer-band-edge" d="M200,712 Q380,702 520,662 L520,668 Q380,706 200,716 Z" fill="var(--white)"/>
    <path class="web-tab" d="M0,712 L190,712 L178,736 L0,736 Z" fill="var(--charcoal)"/>
    <text class="web-tab-text" x="14" y="728">www.meridianpipeline.com.au</text>
  </svg>

  <!-- Front cover -->
  <svg class="cover cover--front" viewBox="0 0 520 736" xmlns="http://www.w3.org/2000/svg">
    <defs>
      <linearGradient id="greenFieldFront" x1="0" y1="0" x2="1" y2="1">
        <stop offset="0" stop-color="var(--brand-green-light)"/>
        <stop offset="1" stop-color="var(--brand-green)"/>
      </linearGradient>
      <linearGradient id="spineShade" x1="0" y1="0" x2="1" y2="0">
        <stop offset="0" stop-color="#000" stop-opacity="0.12"/>
        <stop offset="1" stop-color="#000" stop-opacity="0"/>
      </linearGradient>
      <radialGradient id="thumbGreen"><stop offset="0" stop-color="#8fc33a"/><stop offset="1" stop-color="#e6e6e6"/></radialGradient>
      <radialGradient id="thumbEarth"><stop offset="0" stop-color="#7fbf3a"/><stop offset="1" stop-color="var(--photo-earth)"/></radialGradient>
      <radialGradient id="thumbMachine"><stop offset="0" stop-color="#c0392b"/><stop offset="1" stop-color="#4e9a3a"/></radialGradient>
      <radialGradient id="thumbWorkshop"><stop offset="0" stop-color="#a4a36a"/><stop offset="1" stop-color="#3f4a2e"/></radialGradient>
    </defs>
    <rect class="page-field" width="520" height="736" fill="url(#greenFieldFront)"/>
    <rect class="spine-shade" width="30" height="736" fill="url(#spineShade)"/>

    <g class="brand-lockup">
      <text class="brand-name" x="310" y="108" font-size="46" text-anchor="middle" letter-spacing="4">MERIDIAN</text>
      <text class="brand-name" x="310" y="140" font-size="20" text-anchor="middle" letter-spacing="2">PIPELINE SUPPLIES</text>
    </g>

    <path class="feature-band" d="M0,398 Q330,382 520,140 L520,250 Q350,470 0,476 Z" fill="var(--charcoal)"/>
    <path class="feature-band-edge" d="M0,484 Q355,478 520,262 L520,284 Q365,498 0,496 Z" fill="var(--mist)"/>

    <g class="thumbs" stroke="var(--white)" stroke-width="5">
      <circle cx="82" cy="438" r="32" fill="url(#thumbGreen)" role="img" aria-label="Photo of green lining hoses and fittings"/>
      <circle cx="190" cy="420" r="32" fill="url(#thumbEarth)" role="img" aria-label="Photo of a lined pipe in the ground"/>
      <circle cx="295" cy="370" r="32" fill="url(#thumbMachine)" role="img" aria-label="Photo of a green lining inversion machine"/>
      <circle cx="390" cy="292" r="32" fill="url(#thumbWorkshop)" role="img" aria-label="Photo of equipment in a workshop"/>
    </g>

    <g class="manual-title" text-anchor="middle">
      <text class="title-main" x="360" y="592" font-size="40">INSTRUCTION</text>
      <text class="title-main" x="360" y="614" font-size="15" letter-spacing="9">MANUALS</text>
    </g>

    <path class="web-tab" d="M338,656 L520,656 L520,680 L326,680 Z" fill="var(--charcoal)"/>
    <text class="web-tab-text" x="352" y="672">www.meridianpipeline.com.au</text>
    <path class="footer-band" d="M0,696 L520,688 L520,736 L0,736 Z" fill="var(--silver)"/>
    <path class="footer-band-edge" d="M0,690 L520,682 L520,688 L0,696 Z" fill="var(--white)"/>
  </svg>

</main>
</body>
</html>
```